WINE LABEL for Oak-Q Vale.

We require a wine bottle label for our Oak-Q Vale brand new to the market.
A sample "mock-up" layout of the front and back label is attached. The Oak-Q writing can be a logo type design with any font the designer chooses keeping in mind this will be used on Stationary, business cards and vehicles as well so could included some creative design as long as its clear to read the "Oak-Q" We require a pair of "crusty cowboy boots" as the main theme of the label but the designer could use flair here and design inside a circle or leave as set out.The main thing is they are rugged looking. The label can be framed if appropriate and the use of a parchment look or old western looking idea could be used. We would limit colors to 3 for printing purposes so the combination of colors is up to the designer as long as it stands out on the label visually. The rear label components is attached but can be set-out in any form the designer chooses. The use of the mountain outline at the base of the rear label may add a nice addition to this as its the view we see from our vineyard. Anything else please message me directly.

Target Market(s)

Boutique vineyard label that stands out from the normal.

Contact Information for Business Card

Set out using the designs from the label.

Font styles to use
Other font styles liked:
• Designer to use their selection

Requirements
Must have
• as set out on attached label Mock-up.
• A western theme for the label is preferred.
Should not have
• photos or more than 3 colours

```html
<!DOCTYPE html>
<html lang="en">
<head>
<meta charset="utf-8">
<title>Oak-Q Vale – Pinot Noir Label</title>
<link rel="stylesheet" href="https://fonts.googleapis.com/css2?family=Tinos:wght@400;700&family=Arimo:wght@700&display=swap">
<style>
  :root {
    --backdrop: #000000;
    --paper: #ffffff;
    --ink: #111111;
    --rule: #1a1a1a;
    --oval-line: #3a2a22;
    --gold: #c8913a;
    --gold-light: #e3b15e;
    --vintage-rule: #8b4a3a;
    --sketch-light: #efedea;
    --sketch-dark: #bdbab4;
  }
  * { margin: 0; padding: 0; box-sizing: border-box; }
  html, body {
    width: 1200px; height: 822px; overflow: hidden;
    background: var(--backdrop);
  }
  .canvas { position: relative; width: 1200px; height: 822px; }
  .wine-label {
    position: absolute; left: 365px; top: 116px;
    width: 470px; height: 590px;
    font-family: "Tinos", "Times New Roman", serif;
    color: var(--ink);
    text-align: center;
    line-height: 1;
  }
  .label-shape { position: absolute; left: 0; top: 0; overflow: visible; }
  .label-text { position: absolute; left: 0; right: 0; }
  .brand-name {
    top: 70px;
    font-size: 44px; font-weight: 400; letter-spacing: 1px;
    color: var(--gold);
  }
  .emblem-art {
    position: absolute; left: 128px; top: 152px;
    width: 210px; height: 212px; border-radius: 42% 42% 30% 30%;
    background: radial-gradient(ellipse at 50% 55%, var(--sketch-dark), var(--sketch-light) 62%, transparent 72%);
  }
  .est-label, .est-year { position: absolute; font-size: 19px; }
  .est-label { left: 144px; top: 290px; }
  .est-year { left: 300px; top: 305px; }
  .region {
    top: 375px;
    font-family: "Arimo", Arial, sans-serif; font-weight: 700;
    font-size: 27px; letter-spacing: 0.5px;
  }
  .subregion { top: 405px; font-size: 16px; }
  .vineyard { top: 437px; font-size: 16px; }
  .varietal { top: 458px; font-size: 28px; }
  .origin { top: 488px; font-size: 17px; }
  .vintage {
    position: absolute; left: 198px; top: 518px;
    width: 74px; height: 34px; border-radius: 50%;
    background: radial-gradient(ellipse at 50% 40%, var(--gold-light), var(--gold));
    color: var(--paper); font-size: 22px; line-height: 34px;
  }
</style>
</head>
<body>
<div class="canvas">
  <article class="wine-label">
    <svg class="label-shape" width="470" height="590" viewBox="0 0 470 590" aria-hidden="true">
      <path fill="var(--paper)" d="M22,75 Q235,-75 448,75 A22 22 0 0 0 470,97 L470,505 A22 22 0 0 0 448,527 Q235,647 22,527 A22 22 0 0 0 0,505 L0,97 A22 22 0 0 0 22,75 Z"/>
      <path fill="none" stroke="var(--rule)" stroke-width="2.5" d="M36,87 Q235,-50 434,87 A22 22 0 0 0 458,109 L458,493 A22 22 0 0 0 434,515 Q235,632 36,515 A22 22 0 0 0 12,493 L12,109 A22 22 0 0 0 36,87 Z"/>
      <path fill="none" stroke="var(--rule)" stroke-width="1" d="M40,93 Q235,-38 430,93 A20 20 0 0 0 452,113 L452,489 A20 20 0 0 0 430,509 Q235,622 40,509 A20 20 0 0 0 18,489 L18,113 A20 20 0 0 0 40,93 Z"/>
      <ellipse cx="233" cy="293" rx="126" ry="70" fill="none" stroke="var(--oval-line)" stroke-width="1.8"/>
      <line x1="158" y1="535" x2="198" y2="535" stroke="var(--vintage-rule)" stroke-width="1.2"/>
      <line x1="272" y1="535" x2="312" y2="535" stroke="var(--vintage-rule)" stroke-width="1.2"/>
    </svg>

    <h1 class="label-text brand-name">OAK-Q VALE</h1>
    <div class="emblem-art" role="img" aria-label="Pencil sketch of a pair of rugged cowboy boots with a grape leaf, vine tendrils and a bunch of grapes"></div>
    <span class="est-label">Est</span>
    <span class="est-year">2007</span>

    <p class="label-text region">WAITAKI VALLEY</p>
    <p class="label-text subregion">North Otago</p>
    <p class="label-text vineyard">Single Vineyard</p>
    <p class="label-text varietal">Pinot Noir</p>
    <p class="label-text origin">New Zealand Wine</p>
    <div class="vintage">2016</div>
  </article>
</div>
</body>
</html>
```